Metal tank fabricator website

We need a new website that goes beyond a landing page. We are interested in having some features that will set our website apart form competitors. The first being a tank calculator like the one found at:
https://www.quarnelworks.com/tank-calculator/
We want the first order to be: vertical, horizontal, rectangular.
Animation on the website is wanted for visual appeal, however, we don't want to slow down the loading times of the site. Word Press will be the platform so we can easily manage the content ourselves once it is functional.
This is part of our re branding effort an we are interested in seeing new and fresh ideas.

```html
<!DOCTYPE html>
<html lang="en">
<head>
<meta charset="utf-8">
<title>Ridgeline Tanks – Tank Manufacturer</title>
<link rel="stylesheet" href="https://fonts.googleapis.com/css2?family=Questrial&family=Oswald:wght@300;400&display=swap">
<style>
:root{
  --red:#a8121a;
  --red-dark:#8e0d14;
  --ink:#1a1a1a;
  --text:#444;
  --muted:#666;
  --light:#f1f1f1;
  --line:#d6d6d6;
  --white:#fff;
  --dark:#2b2d30;
}
*{box-sizing:border-box;margin:0;padding:0}
html,body{width:1200px;height:3350px;overflow:hidden}
body{position:relative;background:var(--white);font-family:"Questrial",sans-serif;color:var(--text)}
.abs{position:absolute}
a{color:inherit;text-decoration:none}

/* header */
.brand{left:143px;top:40px;display:flex;align-items:center;gap:10px;font-size:22px;color:var(--ink);letter-spacing:1px}
.brand-mark{width:26px;height:26px;background:var(--ink)}
.call{left:635px;top:31px;font-size:14px;color:var(--ink)}
.call b{color:var(--red);font-weight:400}
.btn{display:inline-block;border-radius:16px;font-size:12px;text-align:center}
.btn-red{background:var(--red);color:var(--white)}
.btn-outline{border:1px solid var(--red);color:var(--red);background:var(--white)}
.enquire{left:824px;top:26px;width:114px;height:28px;line-height:28px}
.social{display:flex;gap:8px}
.social span{width:28px;height:28px;border-radius:50%;border:1px solid var(--red);display:block}
.social span.on{background:var(--red)}
.top-social{left:960px;top:26px}
.nav{left:430px;top:78px;display:flex;font-size:12px;color:var(--ink)}
.nav a{margin-right:40px}
.nav a.active{color:var(--red)}
.nav a:last-child{margin-right:0}

/* hero */
.hero{left:0;top:107px;width:1200px;height:429px;background:linear-gradient(180deg,#6f8fb8 0%,#a9b9cc 45%,#9a9484 70%,#8a7a62 100%)}
.hero h1{position:absolute;left:0;right:0;top:150px;text-align:center;font-weight:400;font-size:25px;line-height:38px;color:var(--white)}
.hero .cta{position:absolute;left:543px;top:244px;width:114px;height:28px;line-height:28px}
.band{left:0;top:536px;width:1200px;height:85px;background:var(--red);color:var(--white)}
.band p{position:absolute;left:143px;top:32px;font-size:16px}
.band .btn{position:absolute;left:928px;top:29px;width:130px;height:28px;line-height:28px;background:var(--white);color:var(--red)}

/* products */
.title{position:absolute;left:0;right:0;text-align:center;font-weight:400;color:var(--ink);font-size:26px}
.tile{position:absolute;background:linear-gradient(180deg,#7ea3cf 0%,#b6c6d8 45%,#b9a887 62%,#9b8866 100%)}
.tile-card{background:var(--red);opacity:.92;color:var(--white);text-align:center;font-size:13px;line-height:22px}
.tile-card p{margin-top:52px}
.tile-card i{display:block;width:28px;height:28px;border-radius:50%;background:var(--white);margin:16px auto 0}

/* about */
.gray{left:0;top:1098px;width:1200px;height:713px;background:var(--light)}
.about-photo{left:250px;top:1273px;width:316px;height:316px;border-radius:50%;background:linear-gradient(180deg,#4f7fc1 0%,#8bb0dc 60%,#6a6a62 100%);box-shadow:0 8px 20px rgba(0,0,0,.25)}
.about h2{font-weight:400;font-size:26px;color:var(--ink)}
.about{left:635px;top:1314px;width:315px}
.about p{margin-top:16px;font-size:11.5px;line-height:17.2px;color:var(--text)}
.about .btn{margin-top:26px;width:114px;height:28px;line-height:26px}
.stat{position:absolute;width:235px;text-align:center}
.stat b{display:block;font-family:"Oswald",sans-serif;font-weight:300;font-size:30px;color:var(--red)}
.stat span{display:block;margin-top:6px;font-size:15px;color:var(--muted)}
.divider{position:absolute;top:1634px;width:1px;height:106px;background:#bbb}

/* why */
.feat{position:absolute;width:240px;text-align:center}
.feat .ico{width:56px;height:56px;border-radius:50%;border:1px solid var(--red);margin:0 auto;display:flex;align-items:center;justify-content:center}
.feat h3{margin-top:20px;font-weight:400;font-size:16px;color:var(--ink)}
.feat p{margin-top:12px;font-size:11.5px;line-height:17px;color:var(--muted)}

/* clients */
.clients{left:0;top:2226px;width:1200px;height:336px;background:linear-gradient(180deg,#3a3c3f 0%,#2a2b2d 70%,#35322d 100%);color:var(--white);text-align:center}
.clients h2{position:absolute;left:0;right:0;top:56px;font-weight:400;font-size:26px}
.clients .q{position:absolute;left:0;right:0;top:106px;font-family:"Oswald",sans-serif;font-size:34px;color:var(--red)}
.clients blockquote{position:absolute;left:250px;width:700px;top:162px;font-style:italic;font-size:14.5px;line-height:22px;color:#ddd}
.clients .who{position:absolute;left:0;right:0;top:248px;font-size:13px;color:var(--red)}
.clients .role{position:absolute;left:0;right:0;top:266px;font-size:11px;color:var(--white)}

/* estimate */
.sub{position:absolute;left:0;right:0;text-align:center;font-size:13px;color:var(--text)}
.sub b{font-weight:400;color:var(--red)}
.field{position:absolute;border:1px solid var(--line);border-radius:14px;font-size:10px;color:#777;padding:9px 14px}

/* footer */
.footer{left:0;top:2964px;width:1200px;height:386px;background:var(--light)}
.f-h{position:absolute;font-size:14px;color:var(--ink)}
.f-t{position:absolute;font-size:11.5px;color:var(--text);line-height:16px}
.f-links{position:absolute;left:454px;top:3074px;font-size:11.5px;line-height:26px;color:var(--text)}
.map{left:614px;top:3033px;width:443px;height:214px;background:linear-gradient(135deg,#cfe4c6 0%,#e9ece4 55%,#f1ede3 100%)}
</style>
</head>
<body>

<!-- header -->
<div class="abs brand"><span class="brand-mark"></span>RIDGELINE TANKS</div>
<div class="abs call"><b>Call Us:</b> (555) 014-2236</div>
<a class="abs btn btn-red enquire">Enquire Now</a>
<div class="abs social top-social" aria-label="Social links"><span></span><span class="on"></span><span></span></div>
<nav class="abs nav">
  <a class="active">Home</a><a>About Us</a><a>Products</a><a>Tank Calculator</a><a>Location</a><a>Testimonials</a><a>Contact Us</a>
</nav>

<!-- hero -->
<section class="abs hero" role="img" aria-label="Row of large vertical steel storage tanks under a blue sky">
  <svg class="abs" style="left:128px;top:204px" width="16" height="26"><path d="M14 1L2 13l12 12" stroke="#fff" stroke-width="2" fill="none"/></svg>
  <svg class="abs" style="left:1042px;top:204px" width="16" height="26"><path d="M2 1l12 12L2 25" stroke="#fff" stroke-width="2" fill="none"/></svg>
  <h1>We are a leading tank manufacturer located<br>in rocky mountain region.</h1>
  <a class="btn btn-red cta">Contact Us</a>
  <svg class="abs" style="left:591px;top:378px" width="18" height="14"><path d="M1 1l8 6 8-6M1 7l8 6 8-6" stroke="#fff" stroke-width="1.5" fill="none"/></svg>
</section>
<section class="abs band">
  <p>We specialize in Monogrammed API-12F Certified tank manufacturing</p>
  <a class="btn">Tank Calculator</a>
</section>

<!-- products -->
<h2 class="title" style="top:686px">Our Products</h2>
<div class="tile" style="left:143px;top:747px;width:443px;height:214px" role="img" aria-label="Tank battery on open prairie"></div>
<div class="tile" style="left:614px;top:747px;width:207px;height:214px" role="img" aria-label="Red production tank detail"></div>
<div class="abs tile-card" style="left:626px;top:757px;width:185px;height:204px"><p>Api-12f 400<br>Bbl Monogrammed<br>Production Tanks</p><i></i></div>
<div class="tile" style="left:850px;top:747px;width:207px;height:214px" role="img" aria-label="Vertical tanks beside a building"></div>
<div class="gray abs"></div>
<div class="tile" style="left:143px;top:990px;width:207px;height:214px" role="img" aria-label="Dark tanks on gravel pad"></div>
<div class="tile" style="left:378px;top:990px;width:208px;height:214px" role="img" aria-label="Horizontal tanks being lifted by crane"></div>
<div class="tile" style="left:614px;top:990px;width:443px;height:214px" role="img" aria-label="Pump jack in an oil field"></div>

<!-- about -->
<div class="abs about-photo" role="img" aria-label="Flag hung between two cranes above the shop yard"></div>
<div class="abs about">
  <h2>About Us</h2>
  <p>Ridgeline Tanks Inc. is a leading tank manufacturer located in Rocky Mountain region. We specialize in Monogrammed API-12F Certified tank manufacturing, tank repair and maintenance. Our production facility location in Northeastern Utah provides us with close proximity to the Utah, Colorado and Wyoming oil and gas fields. We serve the Rocky Mountain region as well as the outlying states including North Dakota.</p>
  <a class="btn btn-outline">Disscover More</a>
</div>
<div class="stat" style="left:129px;top:1652px"><b>150+</b><span>Qualified Workers</span></div>
<div class="divider" style="left:365px"></div>
<div class="stat" style="left:365px;top:1652px"><b>800+</b><span>Projects Delivered</span></div>
<div class="divider" style="left:600px"></div>
<div class="stat" style="left:600px;top:1652px"><b>03</b><span>Locations Worldwide</span></div>
<div class="divider" style="left:836px"></div>
<div class="stat" style="left:836px;top:1652px"><b>500+</b><span>Happy Clients</span></div>

<!-- why -->
<h2 class="title" style="top:1877px">Why Choose Us</h2>
<div class="feat" style="left:167px;top:1942px">
  <div class="ico"><svg width="26" height="16"><path d="M1 9l5 5L15 2M9 14L21 2" stroke="#a8121a" stroke-width="1.5" fill="none"/></svg></div>
  <h3>Quality Products</h3><p>It is a long established fact that a reader will be distracted by the readable content of a page when looking.</p>
</div>
<div class="feat" style="left:480px;top:1942px">
  <div class="ico"><svg width="28" height="20"><rect x="1" y="3" width="16" height="11" fill="none" stroke="#a8121a" stroke-width="1.5"/><path d="M17 7h6l4 4v3H17z" fill="none" stroke="#a8121a" stroke-width="1.5"/><circle cx="7" cy="16" r="2.5" fill="#fff" stroke="#a8121a" stroke-width="1.5"/><circle cx="22" cy="16" r="2.5" fill="#fff" stroke="#a8121a" stroke-width="1.5"/></svg></div>
  <h3>Always Ready To Deliver</h3><p>It is a long established fact that a reader will be distracted by the readable content of a page when looking.</p>
</div>
<div class="feat" style="left:794px;top:1942px">
  <div class="ico"><svg width="20" height="24"><circle cx="10" cy="9" r="7" fill="none" stroke="#a8121a" stroke-width="1.5"/><path d="M5 14l-2 8 4-2 3 3M15 14l2 8-4-2-3 3" fill="none" stroke="#a8121a" stroke-width="1.5"/></svg></div>
  <h3>Reliable Quality</h3><p>It is a long established fact that a reader will be distracted by the readable content of a page when looking.</p>
</div>
<a class="abs btn btn-outline" style="left:543px;top:2128px;width:114px;height:28px;line-height:26px">Enquire Now</a>

<!-- clients -->
<section class="abs clients" role="img" aria-label="Dimmed oil field with pump jacks behind client testimonial">
  <h2>Happy Clients</h2>
  <div class="q">&ldquo;&ldquo;</div>
  <svg class="abs" style="left:143px;top:186px" width="16" height="26"><path d="M14 1L2 13l12 12" stroke="#fff" stroke-width="2" fill="none"/></svg>
  <svg class="abs" style="left:1042px;top:186px" width="16" height="26"><path d="M2 1l12 12L2 25" stroke="#fff" stroke-width="2" fill="none"/></svg>
  <blockquote>&ldquo;There are many variations of passages of Lorem Ipsum available, but the majority have suffered alteration in some form, by injected humour, or randomised words which don't look even slightly believable. If you are going to use a passage of Lorem Ipsum.&rdquo;</blockquote>
  <div class="who">Dale Marrow</div>
  <div class="role">Popular Belief, Lorem Ipsum</div>
</section>

<!-- estimate -->
<h2 class="title" style="top:2620px">Get A Free Esstimate</h2>
<p class="sub" style="top:2656px">Call today: <b>(555) 014-2236</b> or you can also Send Us Message.</p>
<div class="field" style="left:250px;top:2710px;width:221px;height:28px">Your Name</div>
<div class="field" style="left:489px;top:2710px;width:221px;height:28px">Email</div>
<div class="field" style="left:729px;top:2710px;width:221px;height:28px">Phone</div>
<div class="field" style="left:250px;top:2754px;width:700px;height:95px;border-radius:12px;padding-top:12px">Message ...</div>
<a class="abs btn btn-red" style="left:558px;top:2864px;width:85px;height:28px;line-height:28px">Submit</a>

<!-- footer -->
<footer class="abs footer"></footer>
<h4 class="f-h" style="left:143px;top:3032px;font-weight:400">Contact Us</h4>
<p class="f-t" style="left:143px;top:3076px;font-size:13px;color:var(--ink)">Call Us: (555) 014-2236</p>
<p class="f-t" style="left:143px;top:3096px">office@ridgelinetanks.example</p>
<p class="f-t" style="left:143px;top:3128px">Ridgeline Tanks, Inc.<br>1180 Range Road, Basin City, UT, United States</p>
<div class="abs social" style="left:143px;top:3220px"><span></span><span class="on"></span><span></span></div>
<h4 class="f-h" style="left:454px;top:3032px;font-weight:400">Quick Links</h4>
<div class="f-links">Home<br>About Us<br>Products<br>Tank Calculator<br>Location<br>Testimonials<br>Contact Us</div>
<div class="abs map" role="img" aria-label="Area map with a pin marking the shop location"></div>
<p class="f-t" style="left:143px;top:3297px;font-size:11px">© 2020 <span style="color:var(--red)">Ridgeline Tanks, Inc.</span> All Rights Reseved</p>
<p class="f-t" style="left:454px;top:3297px;font-size:11px;color:var(--ink)">Working Hour:&nbsp; Mon-Fri 8am-5pm Mst</p>

</body>
</html>
```